Brightwell Systems - Company Overview Brochure

We would like a single page A4 Brochure to give to new potential customers to provide a quick overview of our company. This will be used in presales meetings.

We have included the content we would like on the brochure under "Brightwell Systems Marketing Brochure.docx".

We have included two other designs "timebundleterms v4.pdf and Brightwell Public Cloud Plans.pdf" which shows similar marketing brochures we have. We would like these designs to have the same Brightwell Blue and "Specialised Technology Consultancy firm" theme.

Target Market(s)

Technology Sector

Industry/Entity Type

Information Technology

Colors
0054AA
0677BA
7BADD7
CADEEF
E8F1F8

Requirements
Must have
• "Innovative Tech Company Theme".

```html
<!DOCTYPE html>
<html lang="en">
<head>
<meta charset="utf-8">
<title>Brightwell Systems – Company Overview Brochure</title>
<link rel="stylesheet" href="https://fonts.googleapis.com/css2?family=Didact+Gothic&family=Poppins:wght@500;600;700&display=swap">
<style>
  :root {
    --stage: #000000;
    --paper: #ffffff;
    --navy: #1d2668;
    --indigo: #2b2f7c;
    --deep: #161c5a;
    --blue: #1e64b4;
    --sky: #45bde9;
    --ink-light: #ffffff;
    --ink-soft: #dfe8f6;
    --box-top: #2f4fa0;
    --box-bottom: #131a58;
  }
  * { box-sizing: border-box; margin: 0; padding: 0; }
  html, body { width: 1200px; height: 847px; overflow: hidden; background: var(--stage); }
  body { position: relative; font-family: "Didact Gothic", "Century Gothic", sans-serif; color: var(--ink-light); }

  .page {
    position: absolute; top: 36px; width: 542px; height: 767px; overflow: hidden;
    background:
      radial-gradient(ellipse at 85% 90%, rgba(40,130,210,.55), transparent 60%),
      radial-gradient(ellipse at 20% 75%, rgba(50,110,200,.35), transparent 55%),
      linear-gradient(160deg, var(--indigo) 0%, #283a8c 45%, var(--blue) 100%);
  }
  .page--services { left: 41px; }
  .page--values { left: 620px; }

  .header-band { position: absolute; left: 0; top: 0; width: 542px; height: 88px; }
  .brand {
    position: absolute; left: 32px; top: 21px; display: flex; align-items: center; gap: 8px;
    font-family: "Poppins", sans-serif; font-weight: 600; font-size: 17px; color: var(--navy);
  }
  .brand-mark { width: 14px; height: 14px; background: var(--navy); }
  .header-tag {
    position: absolute; right: 32px; top: 27px;
    font-family: "Poppins", sans-serif; font-weight: 700; font-size: 12.5px; color: var(--navy); letter-spacing: .1px;
  }

  .body-copy { font-size: 12.4px; line-height: 17.3px; color: var(--ink-soft); }
  .body-copy p + p { margin-top: 5px; }

  .intro { position: absolute; left: 32px; top: 120px; width: 450px; }

  .service-box {
    position: absolute; top: 232px; width: 201px; height: 219px; border-radius: 12px; overflow: hidden;
    background: linear-gradient(180deg, var(--box-top), var(--box-bottom));
    border: 1px solid rgba(255,255,255,.25);
  }
  .service-box--it { left: 55px; }
  .service-box--security { left: 281px; }
  .service-box__title {
    background: var(--sky); text-align: center; font-family: "Poppins", sans-serif; font-weight: 700;
    font-size: 12.5px; line-height: 14px; color: #fff; display: flex; align-items: center; justify-content: center;
  }
  .service-box--it .service-box__title { height: 24px; }
  .service-box--security .service-box__title { height: 38px; }
  .service-grid { display: grid; grid-template-columns: 1fr 1fr; padding: 8px 4px 0; }
  .service-box--security .service-grid { padding-top: 6px; }
  .service { display: flex; flex-direction: column; align-items: center; height: 88px; }
  .service-box--security .service { height: 82px; }
  .service__icon { width: 56px; height: 52px; display: flex; align-items: center; justify-content: center; }
  .service__icon svg { width: 44px; height: 44px; }
  .icon-placeholder { width: 40px; height: 44px; border-radius: 8px; background: linear-gradient(160deg, rgba(255,255,255,.85), rgba(220,230,245,.6)); }
  .service__label {
    margin-top: 6px; text-align: center; font-family: "Poppins", sans-serif; font-weight: 500;
    font-size: 9.4px; line-height: 11.3px; color: #fff;
  }

  .motto { position: absolute; left: 32px; top: 502px; width: 360px; }
  .motto h2 { font-family: "Poppins", sans-serif; font-weight: 600; font-size: 21px; line-height: 26px; color: #fff; margin-bottom: 10px; }

  .server-visual { position: absolute; left: 0; top: 0; width: 542px; height: 767px; pointer-events: none; }

  .values-visual { position: absolute; left: 230px; top: 300px; width: 330px; height: 440px; }

  .section-heading {
    display: flex; align-items: center; gap: 7px;
    font-family: "Poppins", sans-serif; font-weight: 600; font-size: 21px; line-height: 26px; color: #fff;
  }
  .section-heading svg { width: 20px; height: 18px; }
  .commitment { position: absolute; left: 33px; top: 118px; width: 470px; }
  .commitment .section-heading { margin-left: 2px; margin-bottom: 6px; }
  .policy { position: absolute; left: 33px; top: 352px; width: 240px; }
  .policy .section-heading { margin-bottom: 4px; }
  .policy h3 { font-family: "Poppins", sans-serif; font-weight: 600; font-size: 14px; line-height: 18px; color: #fff; margin-top: 4px; }
  .policy .body-copy { margin-bottom: 2px; }

  .terms { position: absolute; left: 33px; top: 718px; width: 470px; font-size: 9.4px; line-height: 11px; color: var(--ink-soft); }
  .terms strong { font-family: "Poppins", sans-serif; font-weight: 600; color: #fff; }
</style>
</head>
<body>

<section class="page page--services">
  <svg class="server-visual" viewBox="0 0 542 767" role="img" aria-label="Photograph of a data centre server aisle inside a triangle">
    <defs>
      <linearGradient id="serverTone" x1="0" y1="0" x2="0" y2="1">
        <stop offset="0" stop-color="#3b4a6a"/>
        <stop offset="1" stop-color="#0c1630"/>
      </linearGradient>
    </defs>
    <polygon points="438,477 542,620 542,767 269,767" fill="url(#serverTone)"/>
    <polygon points="438,639 514,767 362,767" fill="#1e63b3"/>
  </svg>

  <svg class="header-band" viewBox="0 0 542 88" aria-hidden="true">
    <polygon points="0,0 542,0 542,58 98,58 114,88 0,88" fill="#ffffff"/>
  </svg>
  <div class="brand"><span class="brand-mark"></span>Brightwell Systems</div>
  <div class="header-tag">SPECIALISED CONSULTING</div>

  <div class="intro body-copy">
    <p>Brightwell Systems is a Technology Consulting Company based in Perth, Western Australia, which offers customers tailored technical solutions for a range of products.</p>
    <p style="margin-top:5px">Update the below services overview with something better looking.</p>
  </div>

  <div class="service-box service-box--it">
    <div class="service-box__title">IT Services</div>
    <div class="service-grid">
      <div class="service">
        <div class="service__icon"><div class="icon-placeholder" role="img" aria-label="Icon of an engineer with a hard hat"></div></div>
        <div class="service__label">Project<br>Integration</div>
      </div>
      <div class="service">
        <div class="service__icon"><div class="icon-placeholder" role="img" aria-label="Icon of a handshake" style="width:52px;height:34px"></div></div>
        <div class="service__label">Managed<br>Services</div>
      </div>
      <div class="service">
        <div class="service__icon">
          <svg viewBox="0 0 44 44" aria-hidden="true"><path d="M13 20v-6a9 9 0 0 1 18 0v6" fill="none" stroke="#fff" stroke-width="4.5"/><rect x="8" y="19" width="28" height="23" rx="4" fill="#fff"/></svg>
        </div>
        <div class="service__label">Enterprise<br>Security</div>
      </div>
      <div class="service">
        <div class="service__icon">
          <svg viewBox="0 0 44 44" aria-hidden="true">
            <circle cx="15" cy="27" r="9" fill="none" stroke="#fff" stroke-width="6" stroke-dasharray="4 3"/>
            <circle cx="15" cy="27" r="7" fill="none" stroke="#fff" stroke-width="4"/>
            <circle cx="32" cy="14" r="6" fill="none" stroke="#fff" stroke-width="4" stroke-dasharray="3 2.3"/>
            <circle cx="32" cy="14" r="4.5" fill="none" stroke="#fff" stroke-width="3"/>
          </svg>
        </div>
        <div class="service__label">Software<br>Development</div>
      </div>
    </div>
  </div>

  <div class="service-box service-box--security">
    <div class="service-box__title">Electronic Security<br>&amp; Communications</div>
    <div class="service-grid">
      <div class="service">
        <div class="service__icon">
          <svg viewBox="0 0 44 44" aria-hidden="true"><polygon points="8,6 42,20 38,28 4,14" fill="#fff"/><rect x="10" y="24" width="4" height="10" fill="#fff"/><rect x="2" y="32" width="12" height="4" fill="#fff"/></svg>
        </div>
        <div class="service__label">CCTV</div>
      </div>
      <div class="service">
        <div class="service__icon">
          <svg viewBox="0 0 44 44" aria-hidden="true"><path d="M22 3 L39 9 V22 C39 32 31 38 22 42 C13 38 5 32 5 22 V9 Z" fill="#fff"/><circle cx="31" cy="32" r="7" fill="#1e2a70" stroke="#fff" stroke-width="1.5"/><path d="M27.5 32 l2.5 2.5 l4.5 -5" fill="none" stroke="#fff" stroke-width="1.8"/><circle cx="18" cy="18" r="5" fill="none" stroke="#1e2a70" stroke-width="3"/></svg>
        </div>
        <div class="service__label">Integrated Electronic<br>Security</div>
      </div>
      <div class="service">
        <div class="service__icon"><div class="icon-placeholder" role="img" aria-label="Icon of fanned fibre optic cables"></div></div>
        <div class="service__label">Structured<br>Cabling and<br>Fibre Optics</div>
      </div>
      <div class="service">
        <div class="service__icon">
          <svg viewBox="0 0 44 44" aria-hidden="true"><polygon points="22,16 31,42 13,42" fill="#fff"/><circle cx="22" cy="13" r="3" fill="#fff"/><g fill="none" stroke="#fff" stroke-width="2"><path d="M16 7a9 9 0 0 0 0 12"/><path d="M28 7a9 9 0 0 1 0 12"/><path d="M12 4a14 14 0 0 0 0 18"/><path d="M32 4a14 14 0 0 1 0 18"/></g></svg>
        </div>
        <div class="service__label">Wireless<br>Communications</div>
      </div>
    </div>
  </div>

  <div class="motto">
    <h2>Do it Once, Do it Right</h2>
    <div class="body-copy">This can be at the footer, as a backdrop, somewhere large and fancy down the side, middle of the document...<br>Let the designer come up with something.</div>
  </div>
</section>

<section class="page page--values">
  <svg class="values-visual" viewBox="0 0 330 440" role="img" aria-label="Decorative technology graphic of concentric digital rings">
    <defs>
      <radialGradient id="ringGlow" cx="0.68" cy="0.47" r="0.6">
        <stop offset="0" stop-color="#5fa4e6" stop-opacity=".45"/>
        <stop offset=".6" stop-color="#3a7fd0" stop-opacity=".2"/>
        <stop offset="1" stop-color="#2a5fb0" stop-opacity="0"/>
      </radialGradient>
    </defs>
    <rect width="330" height="440" fill="url(#ringGlow)"/>
  </svg>

  <svg class="header-band" viewBox="0 0 542 88" aria-hidden="true">
    <polygon points="0,0 542,0 542,58 98,58 114,88 0,88" fill="#ffffff"/>
  </svg>
  <div class="brand"><span class="brand-mark"></span>Brightwell Systems</div>
  <div class="header-tag">SPECIALISED CONSULTING</div>

  <div class="commitment">
    <h2 class="section-heading"><svg viewBox="0 0 20 18" aria-hidden="true"><path d="M10 1 L19 17 H1 Z" fill="none" stroke="#fff" stroke-width="2"/></svg>Our Commitment</h2>
    <div class="body-copy">
      <p>Our commitment to you is to do things right the first time while being fair but cost-effective. If you’re looking for the cheapest consultants, Brightwell may not be the right fit for you.</p>
      <p>We are a specialised consultancy firm that offers tailored solutions to government and the enterprise sector with some of Perth’s best consultants.</p>
      <p>In areas such as cybersecurity and business continuity, it pays to get it done correctly the first time in alignment with vendor best practices. There are many ways of doing things in the technology field, and only after understanding all methods of achieving an outcome can you recommend the best solution in alignment with best practices.</p>
    </div>
  </div>

  <div class="policy">
    <h2 class="section-heading"><svg viewBox="0 0 20 18" aria-hidden="true"><path d="M10 1 L19 17 H1 Z" fill="none" stroke="#fff" stroke-width="2"/></svg>Our Policy</h2>
    <h3>Be Fair</h3>
    <p class="body-copy">“At Brightwell we believe that both parties benefit when pricing is fair.<br>If margins are too low, we may sacrifice service quality, and this ultimately harms our brand. If margins are too high, our customers have an incentive to seek alternative providers, and this compromises our growth and damages client relationships.”</p>
    <h3>Be Cost-Effective</h3>
    <p class="body-copy">“At Brightwell we believe that it is possible to deliver both high quality at a fair cost, by providing services that are intelligent and efficient.”</p>
  </div>

  <p class="terms">All goods and services provided by Brightwell are provided in accordance with our Standard Terms and Conditions available at <strong>https://www.brightwellsystems.com.au/t&amp;c</strong></p>
</section>

</body>
</html>
```